Certified Probate & Trust Postcard

Hi, I am looking for your assistance. I need a postcard design based on the following specifications. The postcard needs to be 6x9. Here are the specifications for the front and back sides. I also need help incorporating a section on the front of the postcard where I can write the name or names of the people I am addressing the postcard to, as well as a space on the back for the stamp and the receiver's address.

(revised 6/18/2025)
🖼️ FRONT SIDE

(Visual: A serene Bay Area home or warm, sunlit interior. Include Tessa’s headshot. Color palette: ivory, slate, soft gold.)

Headline:

You’ve Taken On So Much — Let Me Help with What Comes Next

Subhead:

Strategic Real Estate Guidance for Probate & Trust
Certified Probate & Trust Specialist | Serving the San Francisco Bay Area

⸻

đź“© BACK SIDE

Opening Quote (italicized):

“I lost both of my parents in 2020 — just weeks apart. That experience shaped how I serve every estate I touch.”

⸻

Main Body Copy:

My name is Tessa Harlow, and I’m a Certified Probate & Trust Specialist who works with families, attorneys, and fiduciaries to guide the real estate side of probate with structure, sensitivity, and strategy.

Whether you’re navigating this with legal support or filing in pro per, this process is layered — emotional, procedural, and often overwhelming. I provide a steady hand when everything else feels uncertain.

With over a decade of experience supporting executives at Corvana, Lumidel, and Dunmore Kass, I bring the same operational precision and discretion to every estate I manage. But I also bring empathy — because I’ve been in your shoes.

⸻

What I Offer — At No Upfront Cost to the Estate:
• Property clean-outs, inspections, and basic preparation — coordinated and covered
• Real estate strategy aligned with court timelines and estate goals
• Hands-on collaboration with attorneys or step-by-step guidance for independent petitioners
• Thoughtful communication that honors your time and your grief

Because real estate isn’t just business.
For you, it’s personal. For me, it’s both.

⸻

Call to Action (in soft gold frame or slate border):

If you’re managing a probate or trust estate and need support you can trust — let’s make this easier, together.
Snapgram: @itstessavoy | CareerNet: profilehub.example/in/tessahomeguide

Industry/Entity Type

Real Estate

Requirements
Must have
• Image needs to have a calm aesthetic (remember the person receiving is grieving) emphasis on luxury as we are looking to attract high end clients so not generic and something that is easily purchased from craftly
Nice to have
• need the following design scheme as it relates to color and font Primary Color Palette: 1. Ecru Stone (Soft Beige/Taupe) – #D7CCC0 • Evokes warmth, trust, and sophistication. 2. Slate Charcoal (Deep Neutral Gray) – #4A4A4A • Represents professionalism, authority, and reliability. Accent Colors: 3. Soft Gold (Understated Elegance) – #C2B280 • Adds a subtle richness without being flashy. 4. Powder White (Clean Background Base) – #FAF9F6 • Used for breathing room, high readability, and elegance. Typography/Callout Highlight Color: 5. Trust Blue (Soft Navy) – #3F4A5F • Often used for headers or key points to add credibility and depth. Tessa Harlow should be in cursive, readable and absolutely beautiful
Should not have
• No yellow, do not use ai on my image,

```html
<!DOCTYPE html>
<html lang="en">
<head>
<meta charset="UTF-8">
<title>Certified Probate &amp; Trust Postcard</title>
<link rel="stylesheet" href="https://fonts.googleapis.com/css2?family=Oswald:wght@600;700&family=Roboto:ital,wght@0,400;0,500;0,700;1,400&display=swap">
<style>
  :root {
    --gold: #bda874;
    --gold-soft: #c9b98a;
    --ink: #1b1b1b;
    --slate: #4a4a4a;
    --navy: #3f4a5f;
    --powder: #faf9f6;
    --stage: #e9e9e9;
    --line: #9a9a9a;
    --photo-top: #8a9db3;
    --photo-bottom: #3f4a5f;
    --portrait: #b9a48f;
  }
  * { box-sizing: border-box; margin: 0; padding: 0; }
  html, body { width: 1200px; height: 3000px; overflow: hidden; }
  body {
    background: var(--stage);
    font-family: "Roboto", Arial, sans-serif;
    color: var(--ink);
    display: flex;
    flex-direction: column;
    align-items: center;
    justify-content: center;
    gap: 100px;
  }
  .postcard {
    position: relative;
    width: 1100px;
    height: 733px;
    background: #ffffff;
    overflow: hidden;
    box-shadow: 0 4px 18px rgba(0,0,0,0.12);
  }

  /* ---------- FRONT ---------- */
  .front-headline-panel {
    position: absolute; left: 0; top: 0; width: 520px; height: 250px;
    background: var(--gold);
    padding: 38px 0 0 48px;
  }
  .front-headline {
    font-family: "Oswald", "Arial Narrow", sans-serif;
    font-weight: 700;
    font-size: 76px;
    line-height: 0.98;
    text-transform: uppercase;
    letter-spacing: 0.5px;
    color: var(--ink);
  }
  .front-ribbon {
    position: absolute; left: 0; top: 250px; width: 580px; height: 66px;
    background: var(--ink);
    clip-path: polygon(0 0, 100% 0, 94% 100%, 0 100%);
    display: flex; align-items: center; padding-left: 48px;
    color: #fff; font-weight: 700; font-size: 26px;
  }
  .service-list { position: absolute; left: 48px; top: 352px; list-style: none; }
  .service-list li {
    display: flex; align-items: center; gap: 16px;
    height: 50px; margin-bottom: 34px;
    font-size: 19px; font-weight: 500; line-height: 1.25; color: var(--ink);
  }
  .icon-badge {
    flex: none; width: 46px; height: 46px; border-radius: 50%;
    background: var(--gold); display: flex; align-items: center; justify-content: center;
  }
  .front-photo {
    position: absolute; left: 520px; top: 0; width: 580px; height: 660px;
    background: linear-gradient(180deg, var(--photo-top) 0%, var(--photo-bottom) 100%);
  }
  .address-box {
    position: absolute; right: 30px; top: 26px; width: 300px; height: 150px;
    background: #fff; border: 1px solid #cfcfcf; padding: 34px 22px 0;
    font-size: 15px; color: var(--slate);
  }
  .address-box .field { display: flex; align-items: flex-end; gap: 8px; margin-bottom: 34px; }
  .address-box .field span.rule { flex: 1; border-bottom: 1px solid var(--line); height: 1px; }
  .headshot {
    position: absolute; left: 458px; top: 420px; width: 136px; height: 136px;
    border-radius: 50%; border: 7px solid var(--gold);
    background: var(--portrait);
  }
  .card-footer {
    position: absolute; left: 0; bottom: 0; width: 100%; height: 73px;
    background: var(--ink); padding: 12px 30px;
  }
  .footer-frame {
    height: 100%; border: 1px solid var(--gold); border-radius: 4px;
    display: flex; align-items: center; justify-content: space-between; padding: 0 16px 0 30px;
  }
  .footer-tagline { color: #fff; font-size: 14px; line-height: 1.3; }
  .social-links { display: flex; gap: 12px; }
  .social-pill {
    display: flex; align-items: center; gap: 8px;
    background: #2b2b2b; border-radius: 18px; padding: 6px 14px 6px 6px;
    color: #fff; font-size: 13px;
  }
  .social-pill .dot { width: 22px; height: 22px; border-radius: 50%; background: var(--gold); }

  /* ---------- BACK ---------- */
  .back-corner {
    position: absolute; left: 0; top: 0; width: 40px; height: 130px;
    background: var(--ink); clip-path: polygon(0 0, 100% 0, 0 100%);
  }
  .back-quote {
    position: absolute; left: 48px; top: 26px; width: 560px;
    font-size: 30px; font-weight: 700; line-height: 1.15; color: var(--navy);
  }
  .back-ribbon {
    position: absolute; left: 0; top: 108px; width: 600px; height: 42px;
    background: var(--ink);
    clip-path: polygon(0 0, 100% 0, 95% 100%, 0 100%);
    display: flex; align-items: center; padding-left: 48px;
    color: #fff; font-size: 16px; font-weight: 500; font-style: italic;
  }
  .stamp-box {
    position: absolute; right: 40px; top: 30px; width: 120px; height: 140px;
    border: 1px solid #bdbdbd;
  }
  .body-copy { position: absolute; left: 48px; top: 172px; width: 600px; }
  .body-copy p { font-size: 12.5px; line-height: 1.45; color: var(--slate); margin-bottom: 9px; }
  .mailing-lines { position: absolute; right: 40px; top: 300px; width: 340px; }
  .mailing-lines span { display: block; border-bottom: 1px solid var(--line); height: 44px; }
  .offer-heading {
    position: absolute; left: 48px; top: 372px;
    font-size: 17px; font-weight: 700; color: var(--navy);
  }
  .offer-grid {
    position: absolute; left: 48px; top: 410px; width: 640px;
    display: grid; grid-template-columns: 1fr 1fr; column-gap: 30px; row-gap: 18px; list-style: none;
  }
  .offer-grid li { display: flex; align-items: center; gap: 12px; font-size: 13px; line-height: 1.35; color: var(--slate); }
  .offer-grid .icon-badge { width: 40px; height: 40px; }
  .cta-band {
    position: absolute; left: 0; top: 572px; width: 640px; height: 72px;
    background: var(--gold-soft);
    clip-path: polygon(0 0, 100% 0, 94% 100%, 0 100%);
    display: flex; align-items: center; padding: 0 70px 0 48px;
    font-size: 17px; font-weight: 700; line-height: 1.3; color: var(--ink);
  }
</style>
</head>
<body>

<section class="postcard postcard-front">
  <div class="front-photo" role="img" aria-label="Photograph of the San Francisco Bay skyline across the water at sunset"></div>

  <div class="front-headline-panel">
    <h1 class="front-headline">You’ve Taken<br>On So Much</h1>
  </div>
  <div class="front-ribbon">Let Me Help with What Comes Next</div>

  <ul class="service-list">
    <li>
      <span class="icon-badge"><svg width="24" height="24" viewBox="0 0 24 24" fill="none" stroke="#1b1b1b" stroke-width="2"><path d="M3 11l9-7 9 7"/><path d="M6 10v10h12V10"/></svg></span>
      <span>Strategic Real Estate<br>Guidance for Probate &amp; Trust</span>
    </li>
    <li>
      <span class="icon-badge"><svg width="24" height="24" viewBox="0 0 24 24" fill="none" stroke="#1b1b1b" stroke-width="2"><path d="M5 12l5 5 9-10"/></svg></span>
      <span>Certified Probate &amp;<br>Trust Specialist</span>
    </li>
    <li>
      <span class="icon-badge"><svg width="24" height="24" viewBox="0 0 24 24" fill="none" stroke="#1b1b1b" stroke-width="2"><path d="M12 21s-7-6.5-7-12a7 7 0 0 1 14 0c0 5.5-7 12-7 12z"/><circle cx="12" cy="9" r="2.5"/></svg></span>
      <span>Serving the San Francisco<br>Bay Area</span>
    </li>
  </ul>

  <div class="address-box">
    <div class="field">Name: <span class="rule"></span></div>
    <div class="field">Address: <span class="rule"></span></div>
  </div>

  <div class="headshot" role="img" aria-label="Headshot of Tessa Harlow"></div>

  <footer class="card-footer">
    <div class="footer-frame">
      <p class="footer-tagline">Because real estate isn’t just business. For you,<br>it’s personal. For me, it’s both.</p>
      <div class="social-links">
        <span class="social-pill"><span class="dot"></span>@itstessavoy</span>
        <span class="social-pill"><span class="dot"></span>profilehub.example/in/tessahomeguide</span>
      </div>
    </div>
  </footer>
</section>

<section class="postcard postcard-back">
  <div class="back-corner"></div>
  <h2 class="back-quote">I lost both of my parents in 2020<br>— just weeks apart.</h2>
  <div class="back-ribbon">That experience shaped how I serve every estate I touch.</div>

  <div class="stamp-box"></div>

  <div class="body-copy">
    <p>My name is Tessa Harlow, and I’m a Certified Probate &amp; Trust Specialist who works with families, attorneys, and fiduciaries to guide the real estate side of probate with structure, sensitivity, and strategy.</p>
    <p>Whether you’re navigating this with legal support or filing in pro per, this process is layered — emotional, procedural, and often overwhelming. I provide a steady hand when everything else feels uncertain.</p>
    <p>With over a decade of experience supporting executives at Corvana, Lumidel, and Dunmore Kass, I bring the same operational precision and discretion to every estate I manage. But I also bring empathy — because I’ve been in your shoes.</p>
  </div>

  <div class="mailing-lines"><span></span><span></span><span></span></div>

  <h3 class="offer-heading">What I Offer — At No Upfront Cost to the Estate:</h3>
  <ul class="offer-grid">
    <li><span class="icon-badge"><svg width="20" height="20" viewBox="0 0 24 24" fill="none" stroke="#1b1b1b" stroke-width="2"><path d="M3 11l9-7 9 7"/><path d="M6 10v10h12V10"/></svg></span>Property clean-outs, inspections, and basic preparation — coordinated and covered</li>
    <li><span class="icon-badge"><svg width="20" height="20" viewBox="0 0 24 24" fill="none" stroke="#1b1b1b" stroke-width="2"><path d="M4 18l6-6 4 4 6-8"/></svg></span>Real estate strategy aligned with court timelines and estate goals</li>
    <li><span class="icon-badge"><svg width="20" height="20" viewBox="0 0 24 24" fill="none" stroke="#1b1b1b" stroke-width="2"><circle cx="8" cy="9" r="3"/><circle cx="16" cy="9" r="3"/><path d="M3 19c1-3 9-3 10 0M11 19c1-3 9-3 10 0"/></svg></span>Hands-on collaboration with attorneys or step-by-step guidance for independent petitioners</li>
    <li><span class="icon-badge"><svg width="20" height="20" viewBox="0 0 24 24" fill="none" stroke="#1b1b1b" stroke-width="2"><path d="M4 5h16v11H9l-5 4z"/></svg></span>Thoughtful communication that honors your time and your grief</li>
  </ul>

  <div class="cta-band">If you’re managing a probate or trust estate and need support you can trust — let’s make this easier, together.</div>

  <footer class="card-footer">
    <div class="footer-frame">
      <p class="footer-tagline">Because real estate isn’t just business. For you,<br>it’s personal. For me, it’s both.</p>
      <div class="social-links">
        <span class="social-pill"><span class="dot"></span>@itstessavoy</span>
        <span class="social-pill"><span class="dot"></span>profilehub.example/in/tessahomeguide</span>
      </div>
    </div>
  </footer>
</section>

</body>
</html>
```